Tequila Startup Company Booklet Design

Need a 16 or so page booklet for a spirits company (like tequila) artfully designed. Need a killer design and beautifully and thoughtfully laid out in a compelling manner. Need talented and creative designer to craft an eye catching booklet.
Updates

Low designer entries

Target Market(s)

Investors and tequila drinkers

Industry/Entity Type

Alcohol spirits distillery

Colors

Requirements
Must have
• Beautiful graphics and photos relevant to agave fields
Nice to have
• Want to emphasize the blue agave fields and the distillery process

```html
<!DOCTYPE html>
<html lang="en">
<head>
<meta charset="utf-8">
<title>Tequila Booklet Spreads</title>
<link href="https://fonts.googleapis.com/css2?family=Archivo:wght@700;800&family=Inter:wght@400&family=EB+Garamond:wght@400&display=swap" rel="stylesheet">
<style>
  :root {
    --paper: #ffffff;
    --ink: #111111;
    --earth: #8b6e5e;
    --earth-deep: #3b2b23;
    --earth-veil: rgba(92, 62, 48, 0.78);
    --light: #ffffff;
  }
  * { margin: 0; padding: 0; box-sizing: border-box; }
  html, body { width: 1200px; height: 2749px; overflow: hidden; background: var(--paper); }
  .canvas { position: relative; width: 1200px; height: 2749px; font-family: "Inter", sans-serif; color: var(--ink); }
  .abs { position: absolute; }
  .photo { position: absolute; }
  .headline { font-family: "Archivo", sans-serif; font-weight: 800; line-height: 1.08; letter-spacing: -0.5px; text-transform: uppercase; }
  .body-copy { font-family: "Inter", sans-serif; font-weight: 400; }

  /* cover */
  .cover { left: 77px; top: 222px; width: 507px; height: 717px; overflow: hidden; }
  .cover-photo { inset: 0; background: linear-gradient(180deg, #dfe6ec 0%, #b9c8d4 14%, #6f8290 24%, #56644f 36%, #6e7a62 46%, #8a9b97 58%, #6d7c78 75%, #5f574a 100%); }
  .cover-band { left: 0; top: 460px; width: 371px; height: 257px; background: var(--earth-veil); }
  .cover-tab { left: 357px; top: 506px; width: 12px; height: 45px; background: var(--light); }
  .cover-title { left: 24px; top: 499px; font-size: 38px; color: var(--light); }
  .cover-tagline { left: 24px; top: 666px; font-family: "EB Garamond", serif; font-size: 15px; color: #e6ddd5; }
  .cover-logo { right: 17px; top: 12px; font-family: "Archivo", sans-serif; font-weight: 700; font-size: 20px; color: var(--light); letter-spacing: -0.5px; }
  .cover-year { right: 17px; bottom: 12px; font-family: "Archivo", sans-serif; font-weight: 700; font-size: 20px; color: var(--light); }

  /* spirit of the land */
  .spirit-block { left: 888px; top: 337px; width: 173px; height: 159px; background: var(--earth); }
  .spirit-photo { left: 654px; top: 395px; width: 389px; height: 260px; background: radial-gradient(circle at 40% 60%, #8a7a5a 0%, #3f4a40 45%, #1f2b2a 100%); }
  .spirit-overlap { left: 888px; top: 395px; width: 155px; height: 101px; background: rgba(40, 28, 22, 0.7); }
  .spirit-title { left: 654px; top: 684px; font-size: 44px; }
  .spirit-text { left: 654px; top: 802px; width: 370px; font-size: 12.6px; line-height: 16.5px; }

  /* where it all begins */
  .begins-photo { left: 252px; top: 1038px; width: 332px; height: 640px; background: linear-gradient(135deg, #3f6a62 0%, #8fb8ab 35%, #c9e0d5 55%, #6e9c8f 75%, #2e4b45 100%); }
  .begins-box { left: 78px; top: 1113px; width: 342px; height: 495px; background: var(--earth); }
  .begins-overlap { left: 252px; top: 1113px; width: 168px; height: 495px; background: rgba(40, 26, 20, 0.82); }
  .begins-title { left: 111px; top: 1162px; font-size: 38px; color: var(--light); }
  .begins-text { left: 111px; top: 1321px; width: 270px; font-size: 15.5px; line-height: 19.5px; color: var(--light); letter-spacing: 0.2px; }

  /* blue agave */
  .agave-box { left: 793px; top: 1044px; width: 291px; height: 610px; background: var(--earth); }
  .agave-photo-top { left: 641px; top: 1082px; width: 270px; height: 255px; background: linear-gradient(180deg, #e6cdb6 0%, #cbb7a4 30%, #6e7c66 55%, #3f4d3c 80%, #55674a 100%); }
  .agave-photo-bottom { left: 641px; top: 1368px; width: 270px; height: 255px; background: linear-gradient(160deg, #4f6a5d 0%, #6f8a74 40%, #5a7040 70%, #3c4a2a 100%); }
  .agave-overlap-top { left: 793px; top: 1082px; width: 118px; height: 255px; background: rgba(38, 26, 20, 0.8); }
  .agave-overlap-bottom { left: 793px; top: 1368px; width: 118px; height: 255px; background: rgba(38, 26, 20, 0.8); }
  .agave-title { left: 928px; top: 1194px; font-size: 25.5px; line-height: 29.5px; color: var(--light); }
  .agave-text { left: 930px; top: 1364px; width: 140px; font-size: 13.5px; line-height: 17px; color: var(--light); }

  /* harvested by masters */
  .masters-title { left: 97px; top: 1862px; font-size: 48px; }
  .masters-text { left: 97px; top: 1989px; width: 460px; font-size: 15.5px; line-height: 19px; }
  .masters-photo { left: 100px; top: 2082px; width: 461px; height: 391px; background: linear-gradient(180deg, #6a6a4a 0%, #4a6a5a 25%, #6b7a6a 50%, #7a5a3a 80%, #4a3424 100%); }

  /* from piña to pour */
  .tile-barrels { left: 609px; top: 1846px; width: 169px; height: 350px; background: linear-gradient(180deg, #c9a45e 0%, #6b5030 30%, #9e8a70 60%, #5a4a3a 100%); }
  .tile-stills { left: 783px; top: 1846px; width: 304px; height: 198px; background: linear-gradient(120deg, #8a5a44 0%, #9a9890 35%, #6f6c66 70%, #8a5a44 100%); }
  .tile-leaf { left: 783px; top: 2048px; width: 132px; height: 148px; background: linear-gradient(135deg, #5f8f80 0%, #a9cbbd 50%, #3f6a5f 100%); }
  .tile-bottling { left: 920px; top: 2048px; width: 167px; height: 333px; background: linear-gradient(180deg, #4a4a48 0%, #d9cdb0 40%, #9a6a2a 70%, #c9871f 100%); }
  .tile-fibre { left: 609px; top: 2200px; width: 306px; height: 181px; background: linear-gradient(180deg, #6a6a70 0%, #8a6a4a 45%, #a87a45 70%, #5a4a40 100%); }
  .pour-title { left: 610px; top: 2422px; font-size: 49px; letter-spacing: -0.3px; }
</style>
</head>
<body>
<main class="canvas">

  <section class="abs cover">
    <div class="photo cover-photo" role="img" aria-label="Blue agave field in front of mountains under a cloudy sky"></div>
    <div class="abs cover-band"></div>
    <div class="abs cover-tab"></div>
    <h1 class="abs headline cover-title">Product<br>Name</h1>
    <p class="abs cover-tagline">Rooted in the Earth. Raised in Fire</p>
    <p class="abs cover-logo">LOGO</p>
    <p class="abs cover-year">2025</p>
  </section>

  <section>
    <div class="abs spirit-block"></div>
    <div class="photo spirit-photo" role="img" aria-label="Aerial view of agave plants on dry soil"></div>
    <div class="abs spirit-overlap"></div>
    <h2 class="abs headline spirit-title">The Spirit of<br>the Land</h2>
    <p class="abs body-copy spirit-text">At [Brand Name], we believe in honoring tradition while crafting with intention. Every drop of our tequila tells the story of the soil, the hands that harvest, and the spirit of celebration.</p>
  </section>

  <section>
    <div class="photo begins-photo" role="img" aria-label="Close-up of blue agave leaves with spines"></div>
    <div class="abs begins-box"></div>
    <div class="abs begins-overlap"></div>
    <h2 class="abs headline begins-title">Where it<br>all begins</h2>
    <p class="abs body-copy begins-text">Born in the heart of Jalisco, our journey began with a single vision: to create tequila that connects people back to nature, heritage, and craft. What started as a family tradition has become a global expression of time, patience, and flavor</p>
  </section>

  <section>
    <div class="abs agave-box"></div>
    <div class="photo agave-photo-top" role="img" aria-label="Hills at dusk with a train passing through agave country"></div>
    <div class="photo agave-photo-bottom" role="img" aria-label="Rows of agave on a green hillside"></div>
    <div class="abs agave-overlap-top"></div>
    <div class="abs agave-overlap-bottom"></div>
    <h2 class="abs headline agave-title">Blue<br>Agave<br>Grown<br>with<br>Purposes</h2>
    <p class="abs body-copy agave-text">We grow only 100% Blue Weber Agave, matured for 6–8 years on volcanic-rich soil at high altitudes. Each piña is a story of sun, soil, and sustainability.</p>
  </section>

  <section>
    <h2 class="abs headline masters-title">Harvested by<br>Masters</h2>
    <p class="abs body-copy masters-text">Our jimadores are artisans of the land—generations of hands that know exactly when to strike. Their expertise ensures the agave is harvested at its peak, with precision and pride</p>
    <div class="photo masters-photo" role="img" aria-label="Jimador in a straw hat harvesting agave with a coa"></div>
  </section>

  <section>
    <div class="photo tile-barrels" role="img" aria-label="Pile of cut agave piñas in a distillery"></div>
    <div class="photo tile-stills" role="img" aria-label="Copper and steel distillation stills"></div>
    <div class="photo tile-leaf" role="img" aria-label="Agave leaf detail"></div>
    <div class="photo tile-bottling" role="img" aria-label="Bottling line filling tequila bottles"></div>
    <div class="photo tile-fibre" role="img" aria-label="Crushed agave fibre on a mill conveyor"></div>
    <h2 class="abs headline pour-title">From Piña to Pour</h2>
  </section>

</main>
</body>
</html>
```